Wall Banner Design (15 & 39 X 50& 39)

Wall Banner 50' long and 15' tall for a Competitive Cheerleading GymLogo IncludedColors we need for the logo: CMY354 green2935 blueColors for the background are up to you. We just cannot artistically warp or symmetrically change the logo. Colors can be moved around though.Wording on the sign - 2 phrases:ONE OF A KIND (Needs to be in CAPS)THE HARBORLIGHT ELITE (needs to be in CAPS)POSSIBLE FONTS TO USE? (Looking for Bold and Fun)-FUTURA CONDENSED BOLD-VARSITY UPPER CASE-VARSITY LOWER CASENeed to create a fun background that incorporates the phrases and the logo and doesn't just look like I created it in PAINT.

Requirements
Must have
• Logo and 2 phrases
Nice to have
• Awesome background
Should not have
• No other logos or phrases

```html
<!DOCTYPE html>
<html lang="en">
<head>
<meta charset="utf-8">
<title>One of a Kind – The Harborlight Elite Wall Banner</title>
<link rel="stylesheet" href="https://fonts.googleapis.com/css2?family=Oswald:wght@500;700&display=swap">
<style>
  :root {
    --navy-deep: #020233;
    --royal: #0a0ac8;
    --cobalt: #0000a8;
    --type-white: #ffffff;
    --logo-green: #12cc12;
  }
  html, body {
    margin: 0;
    padding: 0;
    width: 1200px;
    height: 361px;
    overflow: hidden;
    background: var(--navy-deep);
  }
  .banner {
    position: relative;
    width: 1200px;
    height: 361px;
    overflow: hidden;
  }
  .crowd-backdrop {
    position: absolute;
    inset: 0;
    background:
      radial-gradient(ellipse at 25% 30%, var(--royal) 0%, transparent 55%),
      radial-gradient(ellipse at 75% 60%, var(--cobalt) 0%, transparent 60%),
      linear-gradient(180deg, var(--cobalt) 0%, var(--navy-deep) 100%);
  }
  .phrases {
    position: absolute;
    inset: 0;
    width: 1200px;
    height: 361px;
  }
  .phrase {
    font-family: "Oswald", "Arial Narrow", sans-serif;
    font-weight: 500;
    fill: var(--type-white);
  }
  .team-mark {
    position: absolute;
    left: 455px;
    top: 150px;
    width: 305px;
    height: 90px;
    display: flex;
    align-items: center;
    justify-content: center;
    background: var(--navy-deep);
  }
  .team-mark__name {
    font-family: "Oswald", "Arial Narrow", sans-serif;
    font-weight: 700;
    font-size: 72px;
    line-height: 1;
    letter-spacing: 2px;
    color: var(--logo-green);
  }
</style>
</head>
<body>
  <main class="banner">
    <div class="crowd-backdrop" role="img" aria-label="Blue-toned photo of a cheering cheerleading crowd"></div>

    <svg class="phrases" viewBox="0 0 1200 361" aria-label="One of a kind. The Harborlight Elite.">
      <text class="phrase phrase--top" x="5" y="180" font-size="228" textLength="1190" lengthAdjust="spacingAndGlyphs">ONE OF A KIND</text>
      <text class="phrase phrase--bottom" x="12" y="356" font-size="215" textLength="1178" lengthAdjust="spacingAndGlyphs">THE HARBORLIGHT ELITE</text>
    </svg>

    <div class="team-mark">
      <span class="team-mark__name">GLINTS</span>
    </div>
  </main>
</body>
</html>
```